Bidwell+ WordPress Design

We need a wordpress design that will incorporate a professional color scheme with company logo in a clean layout. The design needs to consider that this will be developed on a responsive theme. Colors are up to the designer - The red of the logo with black, gray or an accent color (maybe the purple of in the photos). Client wants a 'modern' look.

Industry/Entity Type

It Company

Number of Pages Required

1 page

Font styles to use
Serif
Sans Serif

Requirements
Must have
• Navigation: 1) Home 2) Our Auctions 3) Services 4) Buyers & Sellers 5) About Us 6) Contact Us
• Colors - a corporate look with professional color scheme. Red of logo + black and gray, or any other accent that keeps a corporate look. (purple if it looks good)
• In header - logo (attached) , and contact info
• Phone: 555-304-7762 / 555-618-2049
• eMail: holtbidding@quillmail.example
• bidwellplusregion@quillmail.example
• Address: 6218 W Route 842 • Larkfield, TX 48291
• Design will feature a slideshow either full width (960 px) or in the content area - images attached.
• Widgets in sidebar or where appropriate - 1) Email Signup 2) Upcoming Auctions 4) News&Events blog 5) Testimonials 6) Social media - FB, RSS
• Footer will have company logo, association logos (attached) and contact info, with another widget area if necessary
Nice to have
• Use of dropdown menus:
• 1) News&Events and 2) Testimonials under About Us

```html
<!DOCTYPE html>
<html lang="en">
<head>
<meta charset="utf-8">
<title>Bidwell+ — Auctions</title>
<link href="https://fonts.googleapis.com/css2?family=Open+Sans:ital,wght@0,400;0,600;0,700;0,800;1,400&display=swap" rel="stylesheet">
<style>
:root{
  --red:#e0100f;
  --red-dark:#b80a0a;
  --ink:#222;
  --text:#555;
  --muted:#8a8a8a;
  --line:#dcdcdc;
  --panel:#f2f2f2;
  --card:#f1f1f1;
  --btn:#dedede;
  --band:#efefef;
  --footer:#3a3a3a;
  --white:#fff;
  --social-a:#3b5998;
  --social-b:#f48a24;
}
*{box-sizing:border-box;margin:0;padding:0}
html,body{width:1200px;height:2394px;overflow:hidden}
body{font-family:"Open Sans",Arial,sans-serif;color:var(--ink);background:var(--white);position:relative}
a{color:inherit;text-decoration:none}

/* header */
.site-header{height:134px;position:relative}
.brand{position:absolute;left:108px;top:40px;display:flex;align-items:center;gap:10px;font-weight:800;font-size:50px;color:var(--red);letter-spacing:-1px;line-height:1}
.brand-dot{width:14px;height:14px;background:var(--red);border-radius:50%}
.contact{position:absolute;top:50px;display:flex;align-items:center;gap:10px;font-size:13px;color:#555;line-height:22px}
.contact-text{text-align:right}
.contact-icon{width:48px;height:48px;border:2px solid #e2e2e2;border-radius:50%;display:flex;align-items:center;justify-content:center;color:#999}
.contact.mail{right:492px}
.contact.phone{right:322px}
.contact.pin{right:108px}

/* nav */
.main-nav{position:absolute;top:134px;left:0;width:1200px;height:54px;background:var(--red);z-index:3}
.main-nav ul{list-style:none;display:flex;margin-left:108px;height:54px}
.main-nav li{position:relative;border-left:1px solid rgba(0,0,0,.12);color:var(--white);font-size:13.5px;text-transform:uppercase;display:flex;align-items:center;justify-content:center}
.main-nav li:last-child{border-right:1px solid rgba(0,0,0,.12)}
.main-nav li.active{background:var(--red-dark)}
.dropdown{position:absolute;top:54px;left:0;width:155px;background:var(--red-dark);padding:12px 0 10px 0;text-transform:none}
.dropdown div{padding:6px 0 6px 22px;font-size:14px;position:relative}
.dropdown div::before{content:"";position:absolute;left:12px;top:15px;width:4px;height:4px;border-radius:50%;background:var(--white)}

/* slider */
.slider{position:absolute;top:188px;left:0;width:1200px;height:495px;background:linear-gradient(100deg,#b9b7b4 0%,#8e8a92 25%,#5a3f7c 45%,#6c5a80 62%,#aaa8a6 80%,#d2d2d0 100%)}
.slider-arrow{position:absolute;top:228px;width:30px;height:40px;background:rgba(255,255,255,.45);display:flex;align-items:center;justify-content:center}
.slider-arrow.prev{left:0}
.slider-arrow.next{right:0}

/* content */
.latest{position:absolute;left:107px;top:722px;width:685px}
.section-title{font-size:21px;font-weight:400;color:#222;padding-bottom:10px;border-bottom:2px solid #e6e6e6}
.auction-card{background:var(--card);height:228px;margin-top:31px;display:flex;padding:6px}
.auction-card:first-of-type{margin-top:24px}
.auction-thumb{width:235px;height:216px;flex:none}
.auction-body{padding:16px 0 0 16px;width:420px}
.auction-title{font-size:15px;font-weight:400;color:var(--red);line-height:21px}
.auction-date{font-size:13px;color:#222;margin-top:7px}
.auction-text{font-size:11.5px;color:var(--muted);line-height:20px;margin-top:12px}
.btn-more{display:inline-block;background:var(--btn);color:#555;font-size:11.5px;padding:6px 12px;margin-top:16px}
.pagination{display:flex;justify-content:flex-end;gap:15px;margin-top:33px}
.pagination span{width:26px;height:26px;border:1px solid #ccc;font-size:12px;color:#999;display:flex;align-items:center;justify-content:center}
.pagination span.current{background:#666;border-color:#666;color:var(--white)}

/* sidebar */
.sidebar{position:absolute;left:833px;top:715px;width:257px}
.widget{background:var(--panel);margin-bottom:36px}
.widget-title{background:var(--red);color:var(--white);font-size:18px;font-weight:400;height:48px;line-height:48px;padding-left:18px}
.newsletter{padding:13px 13px 13px}
.newsletter-input{background:var(--white);height:40px;font-size:12px;color:#888;padding:12px 16px}
.btn-subscribe{display:block;margin:12px 0 0 auto;width:88px;height:34px;background:#555;color:var(--white);font-size:13px;text-align:center;line-height:34px}
.post-list{padding:20px 13px 0}
.post-item{display:flex;gap:13px;height:110px}
.post-thumb{width:77px;height:83px;flex:none}
.post-excerpt{font-size:11.5px;line-height:17px;color:#333}
.post-more{font-size:11.5px;color:var(--muted);margin-top:9px}
.testimonial{padding:22px 20px 22px}
.quote{font-style:italic;font-size:14px;line-height:25px;color:#333;position:relative;padding-left:20px}
.quote-mark{color:#777;font-weight:800;font-style:normal;font-size:20px}
.quote-author{font-size:12.5px;color:var(--muted);margin-top:14px}
.social{display:flex;gap:14px;margin-top:-10px}
.social span{width:36px;height:36px;border-radius:3px}
.social .social-a{background:var(--social-a)}
.social .social-b{background:var(--social-b)}

/* footer */
.footer-band{position:absolute;top:2163px;left:0;width:1200px;height:116px;background:var(--band)}
.footer-col{position:absolute;top:32px;font-size:14px;color:#222;line-height:22px}
.footer-col .label{font-size:13px;color:#444}
.footer-sep{position:absolute;top:24px;width:1px;height:70px;background:#ccc}
.assoc-label{position:absolute;left:867px;top:48px;font-size:13px;color:#333}
.assoc-badge{position:absolute;top:30px;width:56px;height:56px;background:#2a2a2a}
.assoc-badge.round{border-radius:50%}
.site-footer{position:absolute;top:2279px;left:0;width:1200px;height:115px;background:var(--footer);color:#ccc}
.footer-nav{position:absolute;left:108px;top:30px;display:flex;font-size:13px}
.footer-nav span{padding:0 14px;border-left:1px solid #666}
.footer-nav span:first-child{padding-left:0;border-left:0}
.copyright{position:absolute;left:108px;top:66px;font-size:13px}
.footer-brand{position:absolute;right:110px;top:42px;font-size:34px;font-weight:800;color:#8a8a8a;letter-spacing:-1px}
</style>
</head>
<body>

<header class="site-header">
  <div class="brand"><span>Bidwell+</span><span class="brand-dot"></span></div>

  <div class="contact mail">
    <div class="contact-text">holtbidding@quillmail.example<br>bidwellplusregion@quillmail.example</div>
    <div class="contact-icon"><svg width="16" height="12" viewBox="0 0 16 12"><rect x="0" y="0" width="16" height="12" rx="1" fill="#999"/><path d="M1 1l7 6 7-6" stroke="#fff" stroke-width="1.5" fill="none"/></svg></div>
  </div>
  <div class="contact phone">
    <div class="contact-text">555-304-7762<br>555-618-2049</div>
    <div class="contact-icon"><svg width="16" height="16" viewBox="0 0 24 24"><path d="M6.6 10.8a15 15 0 0 0 6.6 6.6l2.2-2.2a1 1 0 0 1 1-.25 11.4 11.4 0 0 0 3.6.57 1 1 0 0 1 1 1V20a1 1 0 0 1-1 1A17 17 0 0 1 3 4a1 1 0 0 1 1-1h3.5a1 1 0 0 1 1 1c0 1.25.2 2.45.57 3.6a1 1 0 0 1-.25 1z" fill="#999"/></svg></div>
  </div>
  <div class="contact pin">
    <div class="contact-text">6218 W Route 842<br>Larkfield, TX 48291</div>
    <div class="contact-icon"><svg width="14" height="18" viewBox="0 0 14 18"><path d="M7 0a7 7 0 0 0-7 7c0 5 7 11 7 11s7-6 7-11a7 7 0 0 0-7-7z" fill="#999"/><circle cx="7" cy="7" r="2.5" fill="#fff"/></svg></div>
  </div>
</header>

<nav class="main-nav">
  <ul>
    <li style="width:120px">Home</li>
    <li style="width:187px">Our Auctions</li>
    <li style="width:148px">Services</li>
    <li style="width:211px">Buyers &amp; Sellers</li>
    <li class="active" style="width:153px">About Us
      <div class="dropdown"><div>News&amp;Events</div><div>Testimonials</div></div>
    </li>
    <li style="width:158px">Contact Us</li>
  </ul>
</nav>

<section class="slider" role="img" aria-label="Slideshow photo: auction team in purple shirts in front of the auctioneer's stand">
  <div class="slider-arrow prev"><svg width="10" height="16" viewBox="0 0 10 16"><path d="M8 1L2 8l6 7" stroke="#fff" stroke-width="2" fill="none"/></svg></div>
  <div class="slider-arrow next"><svg width="10" height="16" viewBox="0 0 10 16"><path d="M2 1l6 7-6 7" stroke="#fff" stroke-width="2" fill="none"/></svg></div>
</section>

<main class="latest">
  <h2 class="section-title">Latest Auctions</h2>

  <article class="auction-card">
    <div class="auction-thumb" role="img" aria-label="Photo of an antique violin in a worn leather case" style="background:linear-gradient(135deg,#5a3b26,#8e6a4c 50%,#3d2a1c)"></div>
    <div class="auction-body">
      <h3 class="auction-title">Curabitur pellentesque risus magna, in iaculis tellus consequat tempus.</h3>
      <p class="auction-date">June 9, 2015</p>
      <p class="auction-text">Duis a vestibulum libero, nec malesuada arcu. Donec condimen tum felis vitae odio efficitur, at semper ante consequat. Phasellus id leo a massa consectetur aliquam at at ante.</p>
      <a class="btn-more">Read more</a>
    </div>
  </article>

  <article class="auction-card">
    <div class="auction-thumb" role="img" aria-label="Photo of a brass shell-shaped decorative dish" style="background:linear-gradient(135deg,#6b4a2a,#c9a244 50%,#8a6a2e)"></div>
    <div class="auction-body">
      <h3 class="auction-title">Curabitur pellentesque risus magna, in iaculis tellus consequat tempus.</h3>
      <p class="auction-date">June 9, 2015</p>
      <p class="auction-text">Duis a vestibulum libero, nec malesuada arcu. Donec condimen tum felis vitae odio efficitur, at semper ante consequat. Phasellus id leo a massa consectetur aliquam at at ante.</p>
      <a class="btn-more">Read more</a>
    </div>
  </article>

  <article class="auction-card">
    <div class="auction-thumb" role="img" aria-label="Photo of a red vintage car at an outdoor auction" style="background:linear-gradient(180deg,#d8dde2,#a23030 50%,#7c7a70)"></div>
    <div class="auction-body">
      <h3 class="auction-title">Curabitur pellentesque risus magna, in iaculis tellus consequat tempus.</h3>
      <p class="auction-date">June 9, 2015</p>
      <p class="auction-text">Duis a vestibulum libero, nec malesuada arcu. Donec condimen tum felis vitae odio efficitur, at semper ante consequat. Phasellus id leo a massa consectetur aliquam at at ante.</p>
      <a class="btn-more">Read more</a>
    </div>
  </article>

  <article class="auction-card">
    <div class="auction-thumb" role="img" aria-label="Photo of an old brown felt hat" style="background:linear-gradient(180deg,#e8e8e8,#8a6a45 45%,#5c4530)"></div>
    <div class="auction-body">
      <h3 class="auction-title">Curabitur pellentesque risus magna, in iaculis tellus consequat tempus.</h3>
      <p class="auction-date">June 9, 2015</p>
      <p class="auction-text">Duis a vestibulum libero, nec malesuada arcu. Donec condimen tum felis vitae odio efficitur, at semper ante consequat. Phasellus id leo a massa consectetur aliquam at at ante.</p>
      <a class="btn-more">Read more</a>
    </div>
  </article>

  <article class="auction-card">
    <div class="auction-thumb" role="img" aria-label="Photo of a grey fabric sofa with cushions" style="background:linear-gradient(180deg,#e4e2de,#5f5a55 50%,#7a736a)"></div>
    <div class="auction-body">
      <h3 class="auction-title">Curabitur pellentesque risus magna, in iaculis tellus consequat tempus.</h3>
      <p class="auction-date">June 9, 2015</p>
      <p class="auction-text">Duis a vestibulum libero, nec malesuada arcu. Donec condimen tum felis vitae odio efficitur, at semper ante consequat. Phasellus id leo a massa consectetur aliquam at at ante.</p>
      <a class="btn-more">Read more</a>
    </div>
  </article>

  <div class="pagination">
    <span>&laquo;</span><span class="current">1</span><span>2</span><span>3</span><span>4</span><span>5</span><span>&raquo;</span>
  </div>
</main>

<aside class="sidebar">
  <section class="widget">
    <h3 class="widget-title">Newsletter Signup</h3>
    <div class="newsletter">
      <div class="newsletter-input">E-mail</div>
      <a class="btn-subscribe">Subscribe</a>
    </div>
  </section>

  <section class="widget">
    <h3 class="widget-title">Upcoming Auctions</h3>
    <div class="post-list">
      <div class="post-item"><div class="post-thumb" role="img" aria-label="Photo of a pocket watch" style="background:linear-gradient(135deg,#3a3530,#a79a86)"></div><div><p class="post-excerpt">Proin pulvinar justo quis sapien aliquam congue euismod accumsan.</p><p class="post-more">Read more</p></div></div>
      <div class="post-item"><div class="post-thumb" role="img" aria-label="Photo of antique spectacles" style="background:linear-gradient(135deg,#d8d4cc,#6a4a30)"></div><div><p class="post-excerpt">Proin pulvinar justo quis sapien aliquam congue euismod accumsan.</p><p class="post-more">Read more</p></div></div>
      <div class="post-item"><div class="post-thumb" role="img" aria-label="Photo of silver cutlery" style="background:linear-gradient(135deg,#2e2e2e,#bdbdbd)"></div><div><p class="post-excerpt">Proin pulvinar justo quis sapien aliquam congue euismod accumsan.</p><p class="post-more">Read more</p></div></div>
    </div>
  </section>

  <section class="widget">
    <h3 class="widget-title">News &amp; Events</h3>
    <div class="post-list">
      <div class="post-item"><div class="post-thumb" role="img" aria-label="Photo of a colourful puzzle cube" style="background:linear-gradient(135deg,#c23a2a,#2f5fb0 50%,#e0c030)"></div><div><p class="post-excerpt">Proin pulvinar justo quis sapien aliquam congue euismod accumsan.</p><p class="post-more">Read more</p></div></div>
      <div class="post-item"><div class="post-thumb" role="img" aria-label="Photo of a jewelled bracelet" style="background:linear-gradient(135deg,#8a8076,#e0d6c4)"></div><div><p class="post-excerpt">Proin pulvinar justo quis sapien aliquam congue euismod accumsan.</p><p class="post-more">Read more</p></div></div>
      <div class="post-item"><div class="post-thumb" role="img" aria-label="Photo of an amber glass dish" style="background:linear-gradient(135deg,#3a2a1a,#d07a20)"></div><div><p class="post-excerpt">Proin pulvinar justo quis sapien aliquam congue euismod accumsan.</p><p class="post-more">Read more</p></div></div>
    </div>
  </section>

  <section class="widget">
    <h3 class="widget-title">Testimonials</h3>
    <div class="testimonial">
      <p class="quote"><span class="quote-mark" style="position:absolute;left:0;top:-2px">&ldquo;</span>Donec venenatis turpis at enim finibus, sed scelerisque neque placerat. Nunc porttitor nunc ultrices arcu. <span class="quote-mark">&rdquo;</span></p>
      <p class="quote-author">Dana Marsh, Larkfield</p>
    </div>
  </section>

  <div class="social">
    <span class="social-a" role="img" aria-label="Social profile link"></span>
    <span class="social-b" role="img" aria-label="News feed link"></span>
  </div>
</aside>

<section class="footer-band">
  <div class="footer-col" style="left:120px"><div class="label">Address</div>6218 W Route 842<br>Larkfield, TX 48291</div>
  <div class="footer-sep" style="left:308px"></div>
  <div class="footer-col" style="left:356px"><div class="label">Phone</div>555-304-7762<br>555-618-2049</div>
  <div class="footer-sep" style="left:504px"></div>
  <div class="footer-col" style="left:552px"><div class="label">E-mail</div>holtbidding@quillmail.example<br>bidwellplusregion@quillmail.example</div>
  <div class="footer-sep" style="left:811px"></div>
  <div class="assoc-label">Associations</div>
  <div class="assoc-badge round" style="left:958px" role="img" aria-label="State association badge"></div>
  <div class="assoc-badge" style="left:1034px" role="img" aria-label="National association badge"></div>
</section>

<footer class="site-footer">
  <div class="footer-nav"><span>Home</span><span>Our Auctions</span><span>Services</span><span>Buyers &amp; Sellers</span><span>About Us</span><span>Contact Us</span></div>
  <p class="copyright">Copyright &copy; 2015 &nbsp;Bidwell Plus. &nbsp;All rights reserved</p>
  <div class="footer-brand">Bidwell+</div>
</footer>

</body>
</html>
```